Over 100 ladies will be traveling to Ocean City, MD for a Women's Retreat Conference. This flyer is for advertisement. This flyer is to circulate for registrations as well as to post on social media. Theme is Holy Spirit fire. I have attached a photo. All the information in the attachment should be included on the flyer. Information should be clearly readable end eye catching.

Target Market(s)

Church ladies

Industry/Entity Type

Religious

Font styles to use
Sans Serif

Colors

Designer to choose colors to be used in the design.

Requirements
Must have
• Title: Brightvale Womens Gathering 2019 "FIRE"
• All components in attachments

```html
<!DOCTYPE html>
<html lang="en">
<head>
<meta charset="utf-8">
<title>Brightvale Womens Gathering 2019 – FIRE</title>
<link href="https://fonts.googleapis.com/css2?family=Archivo+Black&family=Montserrat:wght@300;400;600;800;900&family=Lato:wght@400;700;900&display=swap" rel="stylesheet">
<style>
:root{
  --page:#e9e6e2;
  --paper:#ffffff;
  --flame:#f2400f;
  --flame-hot:#ff7a1a;
  --ember:#e8380a;
  --ash:#8f8f8f;
  --char:#262626;
  --ink:#2b2b2b;
}
*{margin:0;padding:0;box-sizing:border-box}
html,body{width:1200px;height:1200px;overflow:hidden;background:var(--page)}
.flyer{position:absolute;left:160px;top:30px;width:880px;height:1140px;background:var(--paper);overflow:hidden;box-shadow:0 8px 30px rgba(0,0,0,.18);font-family:"Lato",sans-serif;color:var(--ink)}
.flyer-shapes{position:absolute;inset:0}
.headline{position:absolute;right:40px;top:40px;text-align:right;color:#fff}
.headline__kicker{font-family:"Montserrat",sans-serif;font-weight:300;font-size:40px;letter-spacing:2px;line-height:1}
.headline__event{font-family:"Montserrat",sans-serif;font-size:52px;line-height:1.1;margin-top:4px}
.headline__event b{font-weight:900;letter-spacing:-1px}
.headline__event span{font-weight:300}
.headline__theme{font-family:"Archivo Black",sans-serif;font-size:180px;line-height:.9;color:var(--char);letter-spacing:-4px;margin-top:4px;margin-right:-6px}
.venue{position:absolute;right:50px;top:305px;text-align:right;color:#fff;font-family:"Montserrat",sans-serif;font-weight:800;font-size:21px;line-height:1.25}
.photo{position:absolute;border-radius:50%;border:4px solid #fff}
.photo--beach{left:70px;top:70px;width:170px;height:170px;background:linear-gradient(160deg,#9fc6dc 0%,#e9e2d0 50%,#2f6d9e 100%)}
.photo--tower{left:70px;top:250px;width:170px;height:170px;background:linear-gradient(180deg,#15285a 0%,#1f3468 40%,#e9b98a 60%,#b97a50 100%)}
.photo--room{left:268px;top:385px;width:150px;height:150px;background:linear-gradient(150deg,#cfe0e6 0%,#7fa3b3 55%,#2d5666 100%)}
.photo--lobby{left:440px;top:400px;width:150px;height:150px;background:linear-gradient(150deg,#f1e3a6 0%,#d8b866 50%,#8f6c33 100%)}
.included{position:absolute;left:60px;top:560px}
.included__title{font-family:"Montserrat",sans-serif;font-weight:800;font-size:40px;color:var(--ember);letter-spacing:1px;line-height:1.2}
.included__list{list-style:none;margin-top:6px}
.included__item{display:flex;align-items:center;gap:10px;font-family:"Montserrat",sans-serif;font-weight:600;font-size:22px;line-height:1.6}
.included__item svg{flex:none}
.fine-print{position:absolute;left:60px;top:765px;width:470px;font-size:13.5px;line-height:1.4}
.cost{position:absolute;right:30px;top:470px;width:230px;height:200px;background:var(--char);border-radius:0 0 18px 18px;color:#fff;text-align:center;padding-top:16px}
.cost__label{font-family:"Montserrat",sans-serif;font-weight:400;font-size:28px;letter-spacing:1px}
.cost__amount{font-family:"Archivo Black",sans-serif;font-size:72px;line-height:1}
.cost__amount sup{font-size:38px;vertical-align:top;line-height:1.4}
.cost__note{font-family:"Montserrat",sans-serif;font-weight:600;font-size:17px;line-height:1.2;margin-top:8px}
.speaker{position:absolute;text-align:center}
.speaker__photo{border-radius:50%;border:4px solid var(--ember);margin:0 auto;background:linear-gradient(160deg,#d9d2cc 0%,#a08a7c 55%,#4b3a33 100%)}
.speaker__role{font-family:"Montserrat",sans-serif;font-weight:800;font-size:17px;color:var(--ember);margin-top:6px;line-height:1.2}
.speaker__name{font-size:15px;line-height:1.2}
.speaker__name--solo{margin-top:8px}
.speaker--host{left:270px;top:865px;width:190px}
.speaker--host .speaker__photo{width:140px;height:140px}
.speaker--guest{left:540px;top:760px;width:160px}
.speaker--guest .speaker__photo{width:150px;height:150px}
.speaker--third{right:15px;top:680px;width:170px}
.speaker--third .speaker__photo{width:140px;height:140px}
.callout{position:absolute;left:45px;top:1005px;color:#fff;font-family:"Montserrat",sans-serif}
.callout__lead{font-weight:400;font-size:22px;line-height:1.1}
.callout__action{font-weight:600;font-size:32px;line-height:1.05;margin-top:4px}
.contacts{position:absolute;right:30px;top:995px;text-align:right;font-family:"Montserrat",sans-serif;font-size:22px;line-height:1.8}
.contacts__row{display:flex;justify-content:flex-end;align-items:center;gap:12px}
</style>
</head>
<body>
<main class="flyer">
  <svg class="flyer-shapes" width="880" height="1140" viewBox="0 0 880 1140" aria-hidden="true">
    <defs>
      <linearGradient id="flameFill" x1="0" y1="0" x2="1" y2="1">
        <stop offset="0" stop-color="#e8300c"/>
        <stop offset=".55" stop-color="#ff6a15"/>
        <stop offset="1" stop-color="#f23a0c"/>
      </linearGradient>
      <linearGradient id="emberFill" x1="0" y1="0" x2="0" y2="1">
        <stop offset="0" stop-color="#f23a0c"/>
        <stop offset="1" stop-color="#ff7b1c"/>
      </linearGradient>
    </defs>
    <path d="M150,0 H880 V420 C840,480 760,500 690,470 C610,440 560,370 470,370 C380,370 330,420 250,410 C140,400 95,330 95,230 C95,120 120,40 150,0 Z" fill="#8f8f8f" transform="translate(-10,14)"/>
    <path d="M150,0 H880 V420 C840,480 760,500 690,470 C610,440 560,370 470,370 C380,370 330,420 250,410 C140,400 95,330 95,230 C95,120 120,40 150,0 Z" fill="url(#flameFill)"/>
    <path d="M0,985 C120,955 230,990 280,1060 C320,1100 400,1095 460,1090 C505,1088 520,1110 515,1140 H0 Z" fill="#8f8f8f" transform="translate(6,-12)"/>
    <path d="M0,985 C120,955 230,990 280,1060 C320,1100 400,1095 460,1090 C505,1088 520,1110 515,1140 H0 Z" fill="url(#emberFill)"/>
  </svg>

  <div class="photo photo--beach" role="img" aria-label="Aerial view of the beachfront hotel and ocean"></div>
  <div class="photo photo--tower" role="img" aria-label="Hotel building exterior at dusk"></div>
  <div class="photo photo--room" role="img" aria-label="Hotel guest room with two beds"></div>
  <div class="photo photo--lobby" role="img" aria-label="Hotel lobby with staircase"></div>

  <header class="headline">
    <p class="headline__kicker">BRIGHTVALE WOMENS</p>
    <p class="headline__event"><b>GATHERING</b> <span>2019</span></p>
    <h1 class="headline__theme">FIRE</h1>
  </header>
  <p class="venue">Seabreeze Harbor Hotel &amp; Suites<br>1450 Coastline Ave.<br>Ocean City, Maryland 21800</p>

  <section class="included">
    <h2 class="included__title">INCLUDED:</h2>
    <ul class="included__list">
      <li class="included__item"><svg width="22" height="22" viewBox="0 0 22 22"><circle cx="11" cy="11" r="9" fill="none" stroke="#e8380a" stroke-width="2"/><path d="M6.5,11 l3,3 l6,-6" fill="none" stroke="#e8380a" stroke-width="2"/></svg>All Retreat Sessions</li>
      <li class="included__item"><svg width="22" height="22" viewBox="0 0 22 22"><circle cx="11" cy="11" r="9" fill="none" stroke="#e8380a" stroke-width="2"/><path d="M6.5,11 l3,3 l6,-6" fill="none" stroke="#e8380a" stroke-width="2"/></svg>2 Nights Hotel Accommodations</li>
      <li class="included__item"><svg width="22" height="22" viewBox="0 0 22 22"><circle cx="11" cy="11" r="9" fill="none" stroke="#e8380a" stroke-width="2"/><path d="M6.5,11 l3,3 l6,-6" fill="none" stroke="#e8380a" stroke-width="2"/></svg>1 Hot Lunch Buffet</li>
      <li class="included__item"><svg width="22" height="22" viewBox="0 0 22 22"><circle cx="11" cy="11" r="9" fill="none" stroke="#e8380a" stroke-width="2"/><path d="M6.5,11 l3,3 l6,-6" fill="none" stroke="#e8380a" stroke-width="2"/></svg>1 Full Hot American Breakfast</li>
    </ul>
  </section>

  <p class="fine-print">**ALL deposits/registrations are NON-refundable and NON-transferable. Your entire registration is due by October 1, 2018. Please submit your desired roommate's name at the time of registration. If you do not choose a roommate one will be assigned to you unless you have registered for a private room.</p>

  <aside class="cost">
    <p class="cost__label">COST</p>
    <p class="cost__amount"><sup>$</sup>295</p>
    <p class="cost__note">*Based on double<br>occupancy</p>
  </aside>

  <figure class="speaker speaker--third">
    <div class="speaker__photo" role="img" aria-label="Portrait of retreat speaker"></div>
    <figcaption><p class="speaker__name speaker__name--solo">Pastor Celeste Harmon<br>BGCM - Waldorf, Md</p></figcaption>
  </figure>
  <figure class="speaker speaker--guest">
    <div class="speaker__photo" role="img" aria-label="Portrait of retreat speaker"></div>
    <figcaption><p class="speaker__role">Retreat Speakers</p><p class="speaker__name">Pastor Dalia Monroe<br>Orlando, Florida</p></figcaption>
  </figure>
  <figure class="speaker speaker--host">
    <div class="speaker__photo" role="img" aria-label="Portrait of the retreat host"></div>
    <figcaption><p class="speaker__role">Retreat Host</p><p class="speaker__name">Apostle Renna Caldwell</p></figcaption>
  </figure>

  <div class="callout">
    <p class="callout__lead">For more<br>information</p>
    <p class="callout__action">Call us<br>240-555-0184</p>
  </div>

  <div class="contacts">
    <p class="contacts__row">hello@caldwellministries.org
      <svg width="30" height="30" viewBox="0 0 30 30" aria-hidden="true"><circle cx="15" cy="15" r="15" fill="#e8380a"/><rect x="8" y="10" width="14" height="10" fill="none" stroke="#fff" stroke-width="1.8"/><path d="M8,10 l7,6 l7,-6" fill="none" stroke="#fff" stroke-width="1.8"/></svg></p>
    <p class="contacts__row">brightvale2019.example.com
      <svg width="30" height="30" viewBox="0 0 30 30" aria-hidden="true"><circle cx="15" cy="15" r="15" fill="#e8380a"/><circle cx="15" cy="15" r="7.5" fill="none" stroke="#fff" stroke-width="1.6"/><ellipse cx="15" cy="15" rx="3.2" ry="7.5" fill="none" stroke="#fff" stroke-width="1.4"/><path d="M7.5,15 h15" stroke="#fff" stroke-width="1.4"/></svg></p>
  </div>
</main>
</body>
</html>
```